Tradeora Banner Design for B2B Consulting Firm

Take the already developed logo (attached) and incorporate it into a creative banner design for placement on Tradeora (the social media platform targeting business users). The banner will be used on the firm's company profile page on Tradeora (not yet created).

```html
<!DOCTYPE html>
<html lang="en">
<head>
<meta charset="utf-8">
<title>Tradeora Company Banner Concepts – Verano Crest Advisors</title>
<link rel="stylesheet" href="https://fonts.googleapis.com/css2?family=Crimson+Pro:wght@400;600&family=Roboto:wght@300;400&display=swap">
<style>
  :root {
    --green: #43604a;
    --green-photo: #56755d;
    --green-photo-dark: #3f5c46;
    --grey-photo: #dcdcdc;
    --grey-photo-dark: #cdcdcd;
    --ink: #1e1e1e;
    --brand-blue: #0a66c2;
    --nav-grey: #6b6b6b;
    --rule-grey: #8a8a8a;
    --line-grey: #e3e3e3;
    --paper: #ffffff;
  }
  * { box-sizing: border-box; margin: 0; padding: 0; }
  html, body { width: 1007px; height: 1200px; overflow: hidden; background: var(--paper); }
  .sheet { position: relative; width: 1007px; height: 1200px; overflow: hidden; font-family: "Crimson Pro", serif; }

  .concept { position: absolute; left: 0; width: 1007px; height: 401px; }
  .concept--one { top: 0; }
  .concept--two { top: 401px; }
  .concept--three { top: 803px; height: 397px; }

  .brand {
    position: absolute; left: 95px; top: 50px;
    display: flex; align-items: center; gap: 8px;
    font-weight: 600; font-size: 35px; line-height: 1; color: var(--brand-blue);
  }
  .brand__square { width: 15px; height: 15px; background: var(--brand-blue); }

  .nav { position: absolute; top: 50px; left: 579px; display: flex; font-family: "Roboto", sans-serif; }
  .nav__item {
    position: relative; width: 83px; display: flex; flex-direction: column; align-items: center;
    color: var(--nav-grey); font-size: 12px; font-weight: 300; line-height: 1;
  }
  .nav__item svg { width: 26px; height: 23px; margin-bottom: 9px; }
  .nav__item--active { color: var(--ink); font-weight: 400; }
  .nav__item--active::after { content: ""; position: absolute; left: 9px; right: 9px; top: 45px; height: 2px; background: var(--ink); }
  .nav__divider { position: absolute; left: 912px; top: 45px; width: 1px; height: 53px; background: var(--line-grey); }

  .card {
    position: absolute; left: 96px; top: 132px; width: 812px; height: 269px;
    border-left: 1px solid var(--line-grey); border-right: 1px solid var(--line-grey);
    border-bottom: 3px solid var(--rule-grey);
  }
  .card--open { height: 265px; border-bottom: none; }
  .card--no-left { border-left: none; }

  .banner { position: absolute; overflow: hidden; }
  .banner__title, .banner__sub { position: absolute; text-align: right; white-space: nowrap; line-height: 1; }
  .banner__title { font-size: 24px; letter-spacing: 0.3px; }
  .banner__sub { font-size: 13px; }
  .banner__rule { position: absolute; height: 3px; background: var(--green); }

  .more { position: absolute; right: 27px; top: 161px; display: flex; gap: 3px; }
  .more span { width: 4px; height: 4px; background: #333; }
  .dashes { position: absolute; left: 499px; top: 210px; display: flex; gap: 13px; }
  .dashes span { width: 7px; height: 1px; background: #d6d6d6; }

  .profile {
    position: absolute; left: 122px; width: 132px; height: 129px;
    border: 4px solid var(--paper); box-shadow: 0 1px 5px rgba(0,0,0,0.25);
    display: flex; flex-direction: column; align-items: center; justify-content: center;
  }
  .profile__square { width: 10px; height: 10px; margin-bottom: 10px; }
  .profile__name { font-size: 17px; line-height: 1; }
  .profile__tag { font-size: 7px; letter-spacing: 5px; padding-left: 5px; margin-top: 6px; text-transform: uppercase; line-height: 1; }
  .profile--green { background: var(--green); color: var(--paper); }
  .profile--green .profile__square { background: var(--paper); }
  .profile--white { background: var(--paper); color: var(--green); border: none; }
  .profile--white .profile__square { background: var(--green); }
</style>
</head>
<body>
<div class="sheet">

  <section class="concept concept--one">
    <div class="brand"><span class="brand__square"></span>Tradeora</div>
    <nav class="nav">
      <div class="nav__item"><svg viewBox="0 0 36 32"><rect x="2" y="3" width="32" height="26" fill="none" stroke="#6b6b6b" stroke-width="2.5"/><rect x="7" y="8" width="22" height="4" fill="#6b6b6b"/><rect x="7" y="16" width="9" height="8" fill="#6b6b6b"/><rect x="19" y="16" width="10" height="3" fill="#6b6b6b"/><rect x="19" y="21" width="10" height="3" fill="#6b6b6b"/></svg>Articles</div>
      <div class="nav__item"><svg viewBox="0 0 36 32"><circle cx="12" cy="7" r="6" fill="#6b6b6b"/><rect x="4" y="15" width="16" height="16" rx="2" fill="#6b6b6b"/><circle cx="26" cy="13" r="4.5" fill="#6b6b6b"/><rect x="21" y="20" width="11" height="11" rx="2" fill="#6b6b6b"/></svg>People</div>
      <div class="nav__item"><svg viewBox="0 0 36 32"><rect x="2" y="3" width="32" height="26" fill="none" stroke="#6b6b6b" stroke-width="2.5"/><path d="M14 9 L24 16 L14 23 Z" fill="#6b6b6b"/><rect x="7" y="9" width="4" height="14" fill="#6b6b6b"/></svg>Learning</div>
      <div class="nav__item nav__item--active"><svg viewBox="0 0 36 32"><rect x="12" y="2" width="12" height="6" rx="2" fill="none" stroke="#111" stroke-width="2.5"/><rect x="3" y="8" width="30" height="22" rx="3" fill="#111"/><rect x="3" y="17" width="30" height="2" fill="#fff"/></svg>Jobs</div>
    </nav>
    <div class="nav__divider"></div>

    <div class="card">
      <div class="banner" role="img" aria-label="Green-tinted photo of business people in a meeting"
           style="left:0;top:0;width:810px;height:137px;background:linear-gradient(90deg,var(--green-photo) 0%,#5f7f66 45%,var(--green-photo-dark) 100%);">
        <div class="banner__title" style="right:38px;top:52px;color:var(--paper);">FRACTIONAL MARKETING SERVICES</div>
        <div class="banner__sub" style="right:38px;top:79px;color:var(--paper);">For Private Equity Firms, Family Offices &amp; Investment Banks</div>
      </div>
      <div class="more"><span></span><span></span><span></span></div>
      <div class="dashes"><span></span><span></span><span></span></div>
    </div>
    <div class="profile profile--green" style="top:195px;">
      <div class="profile__square"></div>
      <div class="profile__name">Verano Crest</div>
      <div class="profile__tag">Advisors</div>
    </div>
  </section>

  <section class="concept concept--two">
    <div class="brand"><span class="brand__square"></span>Tradeora</div>
    <nav class="nav">
      <div class="nav__item"><svg viewBox="0 0 36 32"><rect x="2" y="3" width="32" height="26" fill="none" stroke="#6b6b6b" stroke-width="2.5"/><rect x="7" y="8" width="22" height="4" fill="#6b6b6b"/><rect x="7" y="16" width="9" height="8" fill="#6b6b6b"/><rect x="19" y="16" width="10" height="3" fill="#6b6b6b"/><rect x="19" y="21" width="10" height="3" fill="#6b6b6b"/></svg>Articles</div>
      <div class="nav__item"><svg viewBox="0 0 36 32"><circle cx="12" cy="7" r="6" fill="#6b6b6b"/><rect x="4" y="15" width="16" height="16" rx="2" fill="#6b6b6b"/><circle cx="26" cy="13" r="4.5" fill="#6b6b6b"/><rect x="21" y="20" width="11" height="11" rx="2" fill="#6b6b6b"/></svg>People</div>
      <div class="nav__item"><svg viewBox="0 0 36 32"><rect x="2" y="3" width="32" height="26" fill="none" stroke="#6b6b6b" stroke-width="2.5"/><path d="M14 9 L24 16 L14 23 Z" fill="#6b6b6b"/><rect x="7" y="9" width="4" height="14" fill="#6b6b6b"/></svg>Learning</div>
      <div class="nav__item nav__item--active"><svg viewBox="0 0 36 32"><rect x="12" y="2" width="12" height="6" rx="2" fill="none" stroke="#111" stroke-width="2.5"/><rect x="3" y="8" width="30" height="22" rx="3" fill="#111"/><rect x="3" y="17" width="30" height="2" fill="#fff"/></svg>Jobs</div>
    </nav>
    <div class="nav__divider"></div>

    <div class="card card--no-left">
      <div class="banner" role="img" aria-label="Pale greyscale photo of a man working at a desk in an office"
           style="left:304px;top:0;width:507px;height:79px;background:linear-gradient(90deg,#ececea 0%,var(--grey-photo) 60%,#c9c9c7 100%);"></div>
      <div class="banner" style="left:-2px;top:79px;width:813px;height:58px;background:var(--green);"></div>
      <div class="banner__title" style="right:19px;top:50px;color:var(--ink);font-weight:600;">FRACTIONAL MARKETING SERVICES</div>
      <div class="banner__sub" style="right:19px;top:86px;color:var(--paper);">For Private Equity Firms, Family Offices &amp; Investment Banks</div>
      <div class="more"><span></span><span></span><span></span></div>
      <div class="dashes"><span></span><span></span><span></span></div>
    </div>
    <div class="profile profile--white" style="top:211px;height:114px;">
      <div class="profile__square"></div>
      <div class="profile__name">Verano Crest</div>
      <div class="profile__tag">Advisors</div>
    </div>
  </section>

  <section class="concept concept--three">
    <div class="brand"><span class="brand__square"></span>Tradeora</div>
    <nav class="nav">
      <div class="nav__item"><svg viewBox="0 0 36 32"><rect x="2" y="3" width="32" height="26" fill="none" stroke="#6b6b6b" stroke-width="2.5"/><rect x="7" y="8" width="22" height="4" fill="#6b6b6b"/><rect x="7" y="16" width="9" height="8" fill="#6b6b6b"/><rect x="19" y="16" width="10" height="3" fill="#6b6b6b"/><rect x="19" y="21" width="10" height="3" fill="#6b6b6b"/></svg>Articles</div>
      <div class="nav__item"><svg viewBox="0 0 36 32"><circle cx="12" cy="7" r="6" fill="#6b6b6b"/><rect x="4" y="15" width="16" height="16" rx="2" fill="#6b6b6b"/><circle cx="26" cy="13" r="4.5" fill="#6b6b6b"/><rect x="21" y="20" width="11" height="11" rx="2" fill="#6b6b6b"/></svg>People</div>
      <div class="nav__item"><svg viewBox="0 0 36 32"><rect x="2" y="3" width="32" height="26" fill="none" stroke="#6b6b6b" stroke-width="2.5"/><path d="M14 9 L24 16 L14 23 Z" fill="#6b6b6b"/><rect x="7" y="9" width="4" height="14" fill="#6b6b6b"/></svg>Learning</div>
      <div class="nav__item nav__item--active"><svg viewBox="0 0 36 32"><rect x="12" y="2" width="12" height="6" rx="2" fill="none" stroke="#111" stroke-width="2.5"/><rect x="3" y="8" width="30" height="22" rx="3" fill="#111"/><rect x="3" y="17" width="30" height="2" fill="#fff"/></svg>Jobs</div>
    </nav>
    <div class="nav__divider"></div>

    <div class="card card--open">
      <div class="banner" role="img" aria-label="Greyscale photo of colleagues smiling and shaking hands"
           style="left:0;top:0;width:810px;height:137px;background:linear-gradient(90deg,#d4d4d4 0%,#e6e6e6 40%,var(--grey-photo) 70%,var(--grey-photo-dark) 100%);">
        <div class="banner__title" style="right:37px;top:41px;color:var(--ink);">FRACTIONAL MARKETING SERVICES</div>
        <div class="banner__rule" style="left:377px;top:68px;width:397px;"></div>
        <div class="banner__sub" style="right:37px;top:80px;color:var(--ink);">For Private Equity Firms, Family Offices &amp; Investment Banks</div>
      </div>
      <div class="more"><span></span><span></span><span></span></div>
      <div class="dashes"><span></span><span></span><span></span></div>
    </div>
    <div class="profile profile--green" style="top:195px;">
      <div class="profile__square"></div>
      <div class="profile__name">Verano Crest</div>
      <div class="profile__tag">Advisors</div>
    </div>
  </section>

</div>
</body>
</html>
```